Velnadex a Canadian Brand

I'm looking for a new name card design together with our new brand "Velnadex"! FYI, Velnadex is a new developed compounds for raw plastic material in order to improve the Physical properties。

Target Market(s)

Worldwide

Industry/Entity Type

Plastic

```html
<!DOCTYPE html>
<html lang="en">
<head>
<meta charset="utf-8">
<title>Velnadex business card</title>
<link href="https://fonts.googleapis.com/css2?family=Montserrat:wght@400;500;600;700&display=swap" rel="stylesheet">
<style>
  :root {
    --backdrop: #d9d6d2;
    --card-black: #1c1c1d;
    --card-black-deep: #141415;
    --emboss: #262627;
    --brand-red: #e3242b;
    --white: #ffffff;
    --text-light: #f1f1f1;
  }
  * { margin: 0; padding: 0; box-sizing: border-box; }
  html, body {
    width: 1200px;
    height: 716px;
    overflow: hidden;
    background: var(--backdrop);
    font-family: "Montserrat", sans-serif;
  }
  .sheet {
    position: relative;
    width: 1200px;
    height: 716px;
    display: flex;
    align-items: center;
    justify-content: center;
    gap: 60px;
  }
  .card {
    position: relative;
    width: 520px;
    height: 297px;
    background: var(--card-black);
    overflow: hidden;
    box-shadow: 0 6px 18px rgba(0,0,0,0.25);
  }

  /* Front: embossed wordmark */
  .card-front {
    background: var(--card-black-deep);
    display: flex;
    align-items: center;
    justify-content: center;
  }
  .front-wordmark {
    font-weight: 700;
    font-size: 40px;
    letter-spacing: 3px;
    color: var(--emboss);
    text-transform: uppercase;
  }

  /* Back: contact details */
  .brand {
    position: absolute;
    left: 34px;
    top: 34px;
    display: flex;
    align-items: center;
    gap: 10px;
  }
  .brand-mark {
    width: 18px;
    height: 18px;
    background: var(--brand-red);
  }
  .brand-name {
    font-weight: 600;
    font-size: 26px;
    letter-spacing: 1px;
    color: var(--white);
    text-transform: uppercase;
  }
  .person {
    position: absolute;
    left: 34px;
    top: 92px;
  }
  .person-name {
    font-weight: 500;
    font-size: 16px;
    color: var(--brand-red);
    text-transform: uppercase;
    letter-spacing: 0.5px;
  }
  .person-title {
    font-weight: 500;
    font-size: 13px;
    color: var(--text-light);
    margin-top: 2px;
  }
  .contacts {
    position: absolute;
    left: 34px;
    top: 150px;
    list-style: none;
  }
  .contact-item {
    display: flex;
    align-items: center;
    gap: 8px;
    font-size: 14px;
    color: var(--text-light);
    line-height: 22px;
  }
  .contact-icon { width: 11px; height: 11px; flex: none; }
  .address {
    position: absolute;
    right: 26px;
    bottom: 40px;
  }
  .address-label {
    font-size: 14px;
    color: var(--brand-red);
  }
  .address-line {
    font-size: 15px;
    color: var(--text-light);
    margin-top: 2px;
  }
  .bands {
    position: absolute;
    left: 0;
    bottom: 0;
    width: 520px;
    height: 297px;
  }
</style>
</head>
<body>
  <main class="sheet">
    <section class="card card-front" aria-label="Card front">
      <span class="front-wordmark">Velnadex</span>
    </section>

    <section class="card card-back" aria-label="Card back">
      <svg class="bands" viewBox="0 0 520 297" aria-hidden="true">
        <polygon points="0,271 300,271 318,297 0,297" fill="var(--brand-red)"/>
        <polygon points="300,271 520,281 520,297 318,297" fill="var(--white)"/>
      </svg>

      <div class="brand">
        <span class="brand-mark"></span>
        <span class="brand-name">Velnadex</span>
      </div>

      <div class="person">
        <p class="person-name">Your Name</p>
        <p class="person-title">Title</p>
      </div>

      <ul class="contacts">
        <li class="contact-item">
          <svg class="contact-icon" viewBox="0 0 12 12"><rect width="12" height="12" rx="2" fill="var(--brand-red)"/><path d="M3.5 2.8l1.4 1.6-.7.9c.5 1 1.3 1.8 2.3 2.3l.9-.7 1.6 1.4-.8 1.1C5.9 9.2 2.8 6.1 2.4 3.6z" fill="var(--card-black)"/></svg>
          123-456-9999
        </li>
        <li class="contact-item">
          <svg class="contact-icon" viewBox="0 0 12 12"><rect width="12" height="12" rx="2" fill="var(--brand-red)"/><rect x="2.5" y="3.5" width="7" height="5" fill="var(--card-black)"/><path d="M2.5 3.5L6 6.5l3.5-3" stroke="var(--brand-red)" stroke-width="0.8" fill="none"/></svg>
          info@website.com
        </li>
        <li class="contact-item">
          <svg class="contact-icon" viewBox="0 0 12 12"><circle cx="6" cy="6" r="5" fill="none" stroke="var(--brand-red)" stroke-width="1"/><ellipse cx="6" cy="6" rx="2" ry="5" fill="none" stroke="var(--brand-red)" stroke-width="0.8"/><line x1="1" y1="6" x2="11" y2="6" stroke="var(--brand-red)" stroke-width="0.8"/></svg>
          www.website.com
        </li>
      </ul>

      <div class="address">
        <p class="address-label">Address</p>
        <p class="address-line">Lindenweg 14 / 20457 Hamburg</p>
      </div>
    </section>
  </main>
</body>
</html>
```